Chinese Letterhead, artistic Chinese style

I am an obstetrician and gynecologist.
My wife is Chinese.
For my Chinese patients I am looking for a Chinese style stationary, brochure and note card with logo and frame.

I have one in English but now want one in Chinese. - see attached
Text would be English mixed with Chinese.
I envision the design to be soft and feminine, but sincere.
Sweet but not saccharine.
I would like for it to be uniquely appealing to an upscale mainland China clientele, and uniquely Chinese.
At the left top I envision a Chinese character or combo combo - Health - Birth -Beautiful Birth or Gentle Birth.
Format is American US Letter Size.
Updates

Project Deadline Extended Reason: Only two offers. One was a totally unacceptable hasty collage of my own samples.With the other designer there was interaction but her style is just totally different from what I am looking for.I am surprised you have no Chinese designers I could find in your listings. All I found was one lady in Singapore. Added Wednesday, December 30, 2015

Target Market(s)

Chinese pregnant women wanting to give birth in America

Industry/Entity Type

Medical

Font styles to use
Serif
Other font styles liked:
• Calibri, Archer Light Italic, Whitney Light Italic

Colors
85cae6
33b8a4
969696
474747

Requirements
Must have
• Want Chinese style. Can be traditional. Open to any suggestion. I found it very difficult to find a design that features pregnancy and at the same time is tasteful, classy, uplifting.
Nice to have
• A soft, feminine, elegant, artistic touch, pastel colors. A bit dreamy a bit daring.
Should not have
• No pink. No clip art style logos. No clip art like pregnant women. No photos. The picture files are not to be put into the design. I don't own them. They are only meant to be examples to illustrate the style I like

```html
<!DOCTYPE html>
<html lang="en">
<head>
<meta charset="utf-8">
<title>Holden Birth Care – Stationery</title>
<link rel="stylesheet" href="https://fonts.googleapis.com/css2?family=EB+Garamond:wght@400;500&family=Noto+Serif+SC:wght@400;500&display=swap">
<style>
  :root {
    --backdrop: #d8b9a5;
    --paper-cream: #f1ecd9;
    --paper-white: #fbfaf6;
    --ink-dark: #2f2b26;
    --ink-body: #4a453d;
    --ink-soft: #7b7366;
    --rule: #8d8372;
    --wash-dark: #3c3730;
    --wash-light: #cfc8b6;
    --night: #221d2f;
    --night-line: #e9e6ee;
  }
  * { box-sizing: border-box; margin: 0; padding: 0; }
  html, body { width: 1200px; height: 814px; overflow: hidden; }
  body {
    background: var(--backdrop);
    font-family: "EB Garamond", "Times New Roman", serif;
    color: var(--ink-dark);
    position: relative;
  }
  .mark-name { font-family: "EB Garamond", serif; font-weight: 500; color: var(--ink-dark); letter-spacing: .02em; }
  .zh { font-family: "Noto Serif SC", serif; }

  /* Letterhead */
  .letterhead {
    position: absolute; left: 40px; top: 45px; width: 560px; height: 724px;
    background: var(--paper-cream);
  }
  .letterhead .header { position: absolute; left: 70px; top: 62px; display: flex; align-items: flex-start; gap: 18px; }
  .letterhead .header .mark-name { font-size: 34px; line-height: 1; }
  .letterhead .header .name { font-size: 26px; line-height: 1; margin-top: 2px; }
  .letterhead .header .tagline { font-size: 14px; color: var(--ink-body); margin-top: 5px; letter-spacing: .04em; }
  .letterhead .accent-rule { position: absolute; left: 70px; top: 142px; width: 34px; height: 2px; background: var(--rule); }
  .letterhead .body { position: absolute; left: 70px; top: 166px; width: 420px; font-size: 11.5px; line-height: 1.62; color: var(--ink-body); }
  .letterhead .body p + p { margin-top: 12px; }
  .letterhead .signature { position: absolute; left: 290px; top: 440px; font-size: 10.5px; line-height: 1.55; color: var(--ink-body); }
  .letterhead .signature .sig-name { font-size: 13px; color: var(--ink-dark); }
  .letterhead .illustration {
    position: absolute; left: 110px; top: 540px; width: 340px; height: 130px;
    background: radial-gradient(ellipse at 45% 55%, var(--wash-dark) 0%, rgba(60,55,48,.55) 30%, rgba(241,236,217,0) 70%);
  }

  /* Note card */
  .note-card {
    position: absolute; left: 640px; top: 45px; width: 520px; height: 300px;
    background: var(--paper-cream);
  }
  .note-card .divider { position: absolute; left: 190px; top: 22px; bottom: 22px; width: 1px; background: var(--rule); }
  .note-card .contact { position: absolute; left: 26px; top: 32px; width: 158px; }
  .note-card .contact .mark-name { font-size: 26px; display: block; margin-bottom: 18px; }
  .note-card .contact .name { font-size: 17px; margin-bottom: 6px; }
  .note-card .contact .line { font-size: 9.5px; color: var(--ink-body); line-height: 1.6; }
  .note-card .illustration {
    position: absolute; left: 230px; top: 100px; width: 260px; height: 110px;
    background: radial-gradient(ellipse at 45% 50%, var(--wash-light) 0%, rgba(207,200,182,.5) 35%, rgba(241,236,217,0) 72%);
  }

  /* Business card */
  .business-card {
    position: absolute; left: 640px; top: 390px; width: 300px; height: 172px;
    background: var(--paper-white);
  }
  .business-card .mark-box {
    position: absolute; left: 22px; top: 36px; width: 68px; height: 68px;
    border: 1px solid var(--ink-dark); display: flex; align-items: center; justify-content: center;
  }
  .business-card .mark-box .mark-name { font-size: 16px; }
  .business-card .details { position: absolute; left: 106px; top: 38px; }
  .business-card .details .name { font-size: 15px; }
  .business-card .details .title { font-size: 7.5px; color: var(--ink-soft); margin-bottom: 8px; }
  .business-card .details .line { font-size: 9px; line-height: 1.7; color: var(--ink-body); }

  /* Screen mark */
  .screen-mark {
    position: absolute; left: 975px; top: 390px; width: 185px; height: 246px;
    background: var(--night);
  }
  .screen-mark .frame {
    position: absolute; left: 42px; top: 70px; width: 100px; height: 90px;
    border: 1px solid var(--night-line); display: flex; align-items: center; justify-content: center;
  }
  .screen-mark .mark-name { color: var(--night-line); font-size: 20px; }
  .screen-mark .name { position: absolute; left: 0; right: 0; top: 168px; text-align: center; color: var(--night-line); font-size: 12px; }
</style>
</head>
<body>

<section class="letterhead" aria-label="Letterhead">
  <header class="header">
    <span class="mark-name">Holden</span>
    <div>
      <div class="name">Matthias R. Holden</div>
      <div class="tagline zh">嬴先紅形往的受些佳園</div>
    </div>
  </header>
  <div class="accent-rule"></div>
  <div class="body">
    <p>Thank you for choosing our practice for the care of you and your baby. We believe every birth deserves calm, patience and respect, and our team is here to guide you through each step of your pregnancy with warmth and clear advice. Our clinic offers prenatal visits, ultrasound review, birth planning and gentle recovery care, with staff who speak both English and Mandarin so that you and your family always feel heard.</p>
    <p>Please bring your records to the first visit, along with any questions you may have. We will review your history, discuss your wishes for delivery and arrange the tests that suit you. We look forward to welcoming you and to sharing this beautiful time with your family.</p>
  </div>
  <div class="signature">
    <div class="sig-name">Matthias R. Holden</div>
    <div>Certified Obstetrician and Gynecologist</div>
    <div>(812) 555-0147</div>
    <div>m.holden@holdenbirthcare.com</div>
    <div>holdenbirthcare.com</div>
  </div>
  <div class="illustration" role="img" aria-label="Ink-wash painting of a fisherman with cormorants on a bamboo raft"></div>
</section>

<section class="note-card" aria-label="Note card">
  <div class="contact">
    <span class="mark-name">Holden</span>
    <div class="name">Matthias R. Holden</div>
    <div class="line">(812) 555-0147</div>
    <div class="line">m.holden@holdenbirthcare.com</div>
    <div class="line">holdenbirthcare.com</div>
  </div>
  <div class="divider"></div>
  <div class="illustration" role="img" aria-label="Faint ink-wash painting of a fisherman with cormorants on a raft"></div>
</section>

<section class="business-card" aria-label="Business card">
  <div class="mark-box"><span class="mark-name">Holden</span></div>
  <div class="details">
    <div class="name">Matthias R. Holden</div>
    <div class="title">Certified Obstetrician and Gynecologist</div>
    <div class="line">(812) 555-0147</div>
    <div class="line">m.holden@holdenbirthcare.com</div>
    <div class="line">holdenbirthcare.com</div>
  </div>
</section>

<section class="screen-mark" aria-label="Mark on dark ground">
  <div class="frame"><span class="mark-name">Holden</span></div>
  <div class="name">Matthias R. Holden</div>
</section>

</body>
</html>
```